Theater Production Company in Las Vegas

Needing a business card for a theater production company in Las Vegas. We are a full service theatrical production company specializing in Las Vegas entertainment, national
touring shows, and one-off events. From gorilla marketing teams to large scale productions... we do it,and better than anyone.

We like the feel of something hand made and organic.The final design should be creative and communicate that we specialize in theater and special events. We would like to have a design with a front and back.

Hi All,

I want to elaborate on the style of the design that we are hoping for. We are a theater production company in Las Vegas, so the competition is fierce and having a clever business card is incredibly important. 

I am attached a few concepts of a "feel" that would be nice to have conveyed in our card. We love the "worn and vintage" feel that is often seen in antique circus posters. Traditionally, the circus posters are clustered and full of copy - I want a more simplified version of that. Not so cluttered, but with that worn feel. Perhaps even having the card printed on recycled paper to give that textured feel to the visual. 

Example 1 - has a fun worn look, with stars. Some version of this for the back of the card would be fun.
Example 2 - Same things, cool worn feel. Perhaps a small star at the center of the swirl and a little softer on the "grunge".
Example 3 - Has the circus ornament but the colors are nice, not overpowering and again, has that worn feel.
Example 4 - This design isn't as "tight" and cluttered. Has some room to breathe.
Example 5 - I am really liking the look of the this and the above, especially for the back of the card. 

But just to reiterate, the front and face of the card needs to be clear and easy to read. 

Hi Designers, 

I have posted an update so you can have a clearer understanding of what we are needing. I have also increased the funding.

Thank you in advance for your help.

Bridget

Industry/Entity Type

Marketing

Requirements
Must have
• We want to assign creative license. We are creative and hate to be limited by restrictions. Have fun!

The attached files are our logo. One of the files is a business card design that I love. Just a sample of our taste.
Nice to have
• We would like to incorporate: Merchants of the Marquee
as our tagline. I like a vintage, worn feel to the look of designs. Just the word "purveyor" sounds vintage.

```html
<!DOCTYPE html>
<html lang="en">
<head>
<meta charset="utf-8">
<title>Velvet Lantern Productions – Business Card</title>
<link rel="stylesheet" href="https://fonts.googleapis.com/css2?family=Stardos+Stencil:wght@700&family=Old+Standard+TT:wght@700&display=swap">
<style>
  :root {
    --page-bg: #ece8e2;
    --cream: #fbf0cf;
    --blush: #efcfd3;
    --ink: #111111;
    --band: #5f5f5f;
    --band-text: #e2ddd2;
  }
  * { box-sizing: border-box; margin: 0; padding: 0; }
  html, body {
    width: 1200px;
    height: 900px;
    overflow: hidden;
    background: var(--page-bg);
  }
  .sheet {
    width: 1200px;
    height: 900px;
    display: flex;
    align-items: center;
    justify-content: center;
    gap: 40px;
  }
  .card {
    position: relative;
    width: 540px;
    height: 306px;
    overflow: hidden;
    box-shadow: 0 6px 18px rgba(0,0,0,0.25);
    color: var(--ink);
  }
  .card__burst {
    position: absolute;
    inset: 0;
    background:
      radial-gradient(circle at var(--burst-x, 50%) var(--burst-y, 50%),
        var(--cream) 0%, #f8e6d0 45%, var(--blush) 100%);
  }
  .card--front .card__burst { --burst-x: 48%; --burst-y: 10%; }
  .card--back .card__burst { --burst-x: 50%; --burst-y: 50%; }

  .brand {
    position: absolute;
    top: 62px;
    left: 0;
    right: 0;
    display: flex;
    align-items: center;
    justify-content: center;
    gap: 10px;
    font-family: "Stardos Stencil", "Stencil", serif;
    font-weight: 700;
    font-size: 30px;
    line-height: 1;
    letter-spacing: 1px;
    color: var(--ink);
  }
  .brand__dot {
    width: 12px;
    height: 12px;
    border-radius: 50%;
    background: var(--ink);
  }
  .brand__sub {
    position: absolute;
    top: 104px;
    left: 0;
    right: 0;
    text-align: center;
    font-family: "Stardos Stencil", "Stencil", serif;
    font-weight: 700;
    font-size: 10px;
    line-height: 1;
    letter-spacing: 7px;
    color: var(--ink);
  }
  .person-name {
    position: absolute;
    top: 172px;
    left: 0;
    right: 0;
    text-align: center;
    font-family: "Stardos Stencil", "Stencil", serif;
    font-weight: 700;
    font-size: 24px;
    line-height: 1;
    letter-spacing: 0.5px;
  }
  .contact-band {
    position: absolute;
    top: 246px;
    left: 0;
    right: 0;
    height: 16px;
    background: var(--band);
    display: flex;
    align-items: center;
    justify-content: center;
    font-family: "Old Standard TT", serif;
    font-weight: 700;
    font-size: 10.5px;
    line-height: 1;
    letter-spacing: 0.6px;
    white-space: nowrap;
    color: var(--band-text);
  }
  .web-address {
    position: absolute;
    top: 268px;
    left: 0;
    right: 0;
    text-align: center;
    font-family: "Old Standard TT", serif;
    font-weight: 700;
    font-size: 14px;
    line-height: 1;
  }
  .tagline {
    position: absolute;
    top: 50%;
    left: 0;
    right: 0;
    transform: translateY(-50%);
    text-align: center;
    font-family: "Stardos Stencil", "Stencil", serif;
    font-weight: 700;
    font-size: 23px;
    line-height: 1;
    letter-spacing: 0.5px;
  }
</style>
</head>
<body>
  <main class="sheet">
    <section class="card card--front" aria-label="Card front">
      <div class="card__burst" role="img" aria-label="Vintage sunburst rays in cream and blush radiating from the top"></div>
      <div class="brand"><span class="brand__dot"></span><span class="brand__name">Velvet Lantern</span></div>
      <div class="brand__sub">PRODUCTIONS</div>
      <h1 class="person-name">BRIDGET HOLLIS</h1>
      <p class="contact-band">702 555 0148 | 702 555 0193 | 1820 CANYON RIDGE WAY LAS VEGAS, NV 89130</p>
      <p class="web-address">www.velvetlantern.com</p>
    </section>
    <section class="card card--back" aria-label="Card back">
      <div class="card__burst" role="img" aria-label="Vintage sunburst rays in cream and blush radiating from the centre"></div>
      <p class="tagline">MERCHANTS OF THE MARQUEE</p>
    </section>
  </main>
</body>
</html>
```